Business card and stationary for accounting firm
Business card and stationary
Business card and stationary for accounting firm - Financial Services
Creative Brief
Simple
Daniel Brennick
28340 Wexley Parkway Ste 210 Irvine, Ca. 92604
dbrennick@brennickcpa-example.com
brennickcpa-example.com
Looking for simple and professional design for my accounting firm. I also need jpg or other files for header and footers in word for pdf and online printing. Most documents I send would be emailed. Also looking for signature on email messages too.
Not sure but like it simple with maybe my logo and website address.

```html
<!DOCTYPE html>
<html lang="en">
<head>
<meta charset="utf-8">
<title>Brennick CPA Group — Stationery</title>
<link rel="stylesheet" href="https://fonts.googleapis.com/css2?family=Cinzel:wght@500&family=Open+Sans:wght@400;600&display=swap">
<style>
  :root {
    --navy: #1f2b5c;
    --navy-deep: #18224a;
    --charcoal: #2b2b30;
    --paper: #ffffff;
    --paper-shade: #eef0f4;
    --mark-faint: #e6e8ee;
    --ink-soft: #6a7086;
    --backdrop: #ecebe8;
    --label: #555555;
  }
  * { margin: 0; padding: 0; box-sizing: border-box; }
  html, body { width: 1200px; height: 599px; overflow: hidden; }
  body {
    background: var(--backdrop);
    position: relative;
    font-family: "Open Sans", Arial, sans-serif;
  }

  /* brand name lockup */
  .brand { display: flex; align-items: center; gap: 6px; }
  .brand-square { background: var(--navy); flex: none; }
  .brand-name {
    font-family: "Cinzel", Georgia, serif;
    font-weight: 500;
    color: var(--navy);
    white-space: nowrap;
  }
  .brand-tagline {
    font-size: 5px;
    letter-spacing: 0.6px;
    color: var(--ink-soft);
    text-transform: uppercase;
    margin-top: 2px;
  }

  /* business card */
  .business-card {
    position: absolute; left: 24px; top: 233px;
    width: 182px; height: 72px;
    display: flex;
    box-shadow: 0 2px 5px rgba(0,0,0,.2);
  }
  .card-front {
    width: 46%; background: var(--paper);
    display: flex; align-items: center; justify-content: center;
  }
  .card-front .brand-square { width: 7px; height: 7px; }
  .card-front .brand-name { font-size: 7px; }
  .card-back {
    width: 54%; background: var(--navy);
    color: var(--paper);
    padding: 9px 8px;
    font-size: 4.2px; line-height: 1.55;
  }
  .card-back .person { font-size: 6px; font-weight: 600; }
  .card-back .role { opacity: .75; margin-bottom: 4px; }

  /* letterhead */
  .letterhead {
    position: absolute; left: 216px; top: 29px;
    width: 348px; height: 516px;
    background: var(--paper);
    box-shadow: 0 2px 6px rgba(0,0,0,.18);
  }
  .letterhead-header {
    position: absolute; top: 20px; left: 0; right: 0;
    display: flex; flex-direction: column; align-items: center;
  }
  .letterhead-header .brand-square { width: 12px; height: 12px; }
  .letterhead-header .brand-name { font-size: 13px; }
  .letterhead-watermark {
    position: absolute; left: 114px; top: 190px;
    width: 120px; height: 120px;
    background: var(--mark-faint);
    opacity: .7;
  }
  .letterhead-footer {
    position: absolute; left: 0; right: 0; bottom: 0; height: 34px;
    background: var(--navy);
    color: var(--paper);
    font-size: 5px;
    display: flex; flex-direction: column; align-items: center; justify-content: center; gap: 3px;
  }
  .letterhead-footer .footer-line { display: flex; gap: 12px; }

  /* envelopes */
  .envelope-back { position: absolute; left: 680px; width: 460px; }
  .envelope-back svg { display: block; filter: drop-shadow(0 2px 3px rgba(0,0,0,.2)); }
  .envelope-back .seal {
    position: absolute; left: 222px; width: 16px; height: 16px;
  }
  .envelope-navy { top: 19px; }
  .envelope-navy .seal { top: 54px; background: var(--paper); }
  .envelope-charcoal { top: 132px; }
  .envelope-charcoal .seal { top: 54px; background: var(--navy); }
  .envelope-white { top: 240px; }
  .envelope-white .seal { top: 40px; background: var(--navy); }

  .envelope-front {
    position: absolute; left: 655px; top: 360px;
    width: 492px; height: 176px;
    background: var(--paper);
    box-shadow: 0 2px 6px rgba(0,0,0,.2);
    overflow: hidden;
  }
  .envelope-front .return-address { position: absolute; left: 18px; top: 18px; }
  .envelope-front .brand-square { width: 12px; height: 12px; }
  .envelope-front .brand-name { font-size: 13px; }
  .envelope-front .address-line { font-size: 5px; color: var(--ink-soft); margin-top: 3px; }
  .envelope-watermark {
    position: absolute; left: 330px; top: 40px;
    width: 120px; height: 120px;
    background: var(--mark-faint);
    opacity: .7;
  }

  .piece-label {
    position: absolute; top: 568px;
    font-size: 7px; letter-spacing: 1px; color: var(--label);
  }
</style>
</head>
<body>

  <section class="business-card" aria-label="Business card">
    <div class="card-front">
      <div class="brand"><span class="brand-square"></span><span class="brand-name">Brennick CPA Group</span></div>
    </div>
    <div class="card-back">
      <p class="person">Daniel Brennick</p>
      <p class="role">Managing Partner</p>
      <p>28340 Wexley Parkway Ste 210 Irvine, Ca. 92604</p>
      <p>dbrennick@brennickcpa-example.com</p>
      <p>brennickcpa-example.com</p>
      <p>harborviewledger</p>
    </div>
  </section>

  <section class="letterhead" aria-label="Letterhead">
    <header class="letterhead-header">
      <div class="brand"><span class="brand-square"></span><span class="brand-name">Brennick CPA Group</span></div>
      <p class="brand-tagline">Certified Public Accountants and Business Advisors</p>
    </header>
    <div class="letterhead-watermark"></div>
    <footer class="letterhead-footer">
      <p>28340 Wexley Parkway Ste 210 Irvine, Ca. 92604</p>
      <p class="footer-line"><span>dbrennick@brennickcpa-example.com</span><span>brennickcpa-example.com</span></p>
    </footer>
  </section>

  <div class="envelope-back envelope-navy">
    <svg width="460" height="140" viewBox="0 0 460 140">
      <rect width="460" height="140" fill="var(--navy-deep)"/>
      <path d="M0 0 H460 V8 L246 80 Q230 86 214 80 L0 8 Z" fill="var(--navy)"/>
    </svg>
    <span class="seal"></span>
  </div>

  <div class="envelope-back envelope-charcoal">
    <svg width="460" height="140" viewBox="0 0 460 140">
      <rect width="460" height="140" fill="#3a3a40"/>
      <path d="M0 0 H460 V8 L246 80 Q230 86 214 80 L0 8 Z" fill="var(--charcoal)"/>
    </svg>
    <span class="seal"></span>
  </div>

  <div class="envelope-back envelope-white">
    <svg width="460" height="125" viewBox="0 0 460 125">
      <rect width="460" height="125" fill="var(--paper-shade)"/>
      <path d="M0 0 H460 V6 L246 68 Q230 73 214 68 L0 6 Z" fill="var(--paper)" stroke="#d8dbe2" stroke-width="1"/>
    </svg>
    <span class="seal"></span>
  </div>

  <section class="envelope-front" aria-label="Envelope front">
    <div class="return-address">
      <div class="brand"><span class="brand-square"></span><span class="brand-name">Brennick CPA Group</span></div>
      <p class="address-line">28340 Wexley Parkway Ste 210 Irvine, Ca. 92604</p>
    </div>
    <div class="envelope-watermark"></div>
  </section>

  <p class="piece-label" style="left:352px;">Letter Head: Option 1</p>
  <p class="piece-label" style="left:868px;">Envelope Option 3</p>

</body>
</html>
```